Music Festival in Colorado Needs Awesome Flier Design

We need an eye-catching & captivating flier design for an annual music festival in Denver, CO (USA). The festival features the best Colorado musicians within the genres of jam - funk - bluegrass - electronic - reggae - rock.

The design should look clean and professional while still being creative and unique. The past three years' flier designs are attached, as well as the logo and some other designs that match the aesthetic of what we're looking for.

This festival has a big element of Colorado pride so any

Target Market(s)

Hippies - live music enthusiasts - partiers. Ages 21 - 40.

Industry/Entity Type

Entertainment

Colors
0355a3
ec1f27
ffffff
fbed22

Requirements
Must have
• Attached design text.
Nice to have
• - Quality texture and psychedelic elements.
• - Colorado pride elements; color scheme (red, white, blue & yellow), flag, ect.
• - Nature elements are awesome but this is also a downtown festival so keep that in mind.
Should not have
• Cheesy artwork.

```html
<!DOCTYPE html>
<html lang="en">
<head>
<meta charset="utf-8">
<title>Pass the Sound – 6th Annual Festival Flier</title>
<link rel="stylesheet" href="https://fonts.googleapis.com/css2?family=Jost:wght@300;400;600;700&display=swap">
<style>
  :root {
    --paper: #ffffff;
    --night-top: #1b2134;
    --night-mid: #3b3f55;
    --night-low: #8b8898;
    --band-blue: #4e8ca4;
    --ink-light: #dcdce0;
    --ink-soft: #c6c5cc;
    --rule: #b9b8c0;
    --ridge-light: #6fa8bb;
    --ridge-deep: #2d5a70;
    --skyline: #1a2030;
  }
  * { box-sizing: border-box; margin: 0; padding: 0; }
  html, body { width: 796px; height: 1200px; overflow: hidden; background: var(--paper); }
  .flier {
    position: absolute; left: 26px; top: 26px; width: 744px; height: 1148px;
    background: linear-gradient(180deg, var(--night-top) 0%, var(--night-top) 28%, var(--night-mid) 55%, var(--night-low) 80%);
    font-family: "Jost", "Futura", sans-serif;
    color: var(--ink-light);
    text-align: center;
    overflow: hidden;
  }
  .top-band { position: absolute; left: 0; top: 26px; width: 100%; height: 14px; background: var(--band-blue); }
  .edition { position: absolute; top: 62px; width: 100%; font-weight: 400; font-size: 18px; letter-spacing: 2px; }
  .festival-name { position: absolute; top: 92px; width: 100%; font-weight: 700; color: var(--ink-light); text-transform: uppercase; }
  .festival-name .name-top { display: block; font-size: 50px; line-height: 50px; letter-spacing: 1px; }
  .festival-name .name-main { display: block; font-size: 160px; line-height: 150px; letter-spacing: -4px; }
  .tagline { position: absolute; top: 312px; width: 100%; font-weight: 600; font-size: 17px; letter-spacing: 4px; text-transform: uppercase; color: var(--ink-light); }
  .rule { position: absolute; left: 108px; width: 528px; height: 2px; background: var(--rule); }
  .rule.upper { top: 362px; }
  .rule.lower { top: 746px; }
  .lineup { position: absolute; top: 380px; width: 100%; list-style: none; text-transform: uppercase; }
  .lineup li { white-space: nowrap; }
  .act-headliner { font-weight: 600; font-size: 52px; letter-spacing: 1px; height: 52px; line-height: 52px; }
  .act-light { font-weight: 300; font-size: 46px; letter-spacing: 0; }
  .act-bold-small { font-weight: 700; font-size: 27px; height: 22px; line-height: 22px; }
  .act-bold-large { font-weight: 600; font-size: 50px; letter-spacing: 1px; height: 48px; line-height: 48px; }
  .act-light-small { font-weight: 400; font-size: 26px; letter-spacing: 1px; height: 34px; line-height: 34px; color: var(--ink-soft); }
  .lineup .h58 { height: 58px; line-height: 58px; }
  .lineup .h56 { height: 56px; line-height: 56px; }
  .lineup .h54 { height: 54px; line-height: 54px; }
  .lineup .h28 { height: 28px; line-height: 28px; }
  .tickets { position: absolute; top: 758px; width: 100%; font-size: 18px; font-weight: 400; color: var(--ink-soft); z-index: 2; }
  .scene { position: absolute; left: 0; top: 790px; width: 100%; height: 358px; }
  .venue { position: absolute; bottom: 18px; width: 100%; font-weight: 600; font-size: 15px; letter-spacing: 1px; color: var(--paper); }
</style>
</head>
<body>
<main class="flier">
  <div class="top-band"></div>
  <p class="edition">- 6TH ANNUAL -</p>
  <h1 class="festival-name"><span class="name-top">Pass the</span><span class="name-main">Sound</span></h1>
  <p class="tagline">Colorado Music Festival</p>

  <div class="rule upper"></div>
  <ul class="lineup">
    <li class="act-headliner">Reed Calder Band</li>
    <li class="act-light h58">All Hands Orchestra</li>
    <li class="act-bold-small">Fault Theory &bull; The Copper Sprouts</li>
    <li class="act-light h56">J-Ray &amp; The Summit</li>
    <li class="act-bold-large">Wapiti &middot; Allele</li>
    <li class="act-light h54">Prominence Ensemble</li>
    <li class="act-bold-small h28">Skyhued &nbsp; Metatonics &nbsp; Specular</li>
    <li class="act-light-small">Clear Dream &nbsp; Relay Station &nbsp; Orbits</li>
  </ul>
  <div class="rule lower"></div>
  <p class="tickets">Tickets &amp; More Info @ www.passthesoundfest.com</p>

  <svg class="scene" role="img" aria-label="Illustration of blue mountain ridges under a full moon, with pine trees and a city skyline silhouette" viewBox="0 0 744 358" preserveAspectRatio="none">
    <defs>
      <linearGradient id="scene-fill" x1="0" y1="0" x2="0" y2="1">
        <stop offset="0" stop-color="var(--ridge-light)" stop-opacity="0"/>
        <stop offset="0.18" stop-color="var(--ridge-light)" stop-opacity="0.85"/>
        <stop offset="0.5" stop-color="var(--ridge-deep)"/>
        <stop offset="0.8" stop-color="var(--skyline)"/>
        <stop offset="1" stop-color="var(--skyline)"/>
      </linearGradient>
    </defs>
    <rect width="744" height="358" fill="url(#scene-fill)"/>
  </svg>

  <p class="venue">LARCH YARD COMPOUND - DENVER, CO 80221 - 418 W. 52ND AVE</p>
</main>
</body>
</html>
```